Business Card Design Project

Logo, Phone Number, slogan, must be included on front of card. Services must be listed: Lawn Service, Fertilization, Pool Service, Pressure Washing. and a space to "write in" salesmans name.
Slogan "Your Everything Outside Company"
Phone: 602-417-3859
Email: brightacreyard@mailnest.net
Looking for a bold yet simple design to enforce brand recognition.

Target Market(s)

Middle to upper class US homeowners

Industry/Entity Type

Business

Requirements
Must have
• Logo, Phone, and Slogan on front
Should not have
• cluttered background

Files

```html
<!DOCTYPE html>
<html lang="en">
<head>
<meta charset="utf-8">
<title>Brightacre Services – Business Card</title>
<link rel="stylesheet" href="https://fonts.googleapis.com/css2?family=Marcellus+SC&family=Kalam:wght@400&display=swap">
<style>
  :root {
    --backdrop: #e6e0da;
    --card-white: #ffffff;
    --brand-blue: #2f5d9c;
    --brand-blue-deep: #244a80;
    --brand-green: #8cbf3f;
    --text-blue: #2c4f86;
    --line-light: rgba(255,255,255,0.75);
  }
  * { box-sizing: border-box; margin: 0; padding: 0; }
  html, body {
    width: 1200px; height: 720px; overflow: hidden;
    background: var(--backdrop);
  }
  .canvas {
    position: relative; width: 1200px; height: 720px;
    display: flex; align-items: center; justify-content: center; gap: 60px;
  }
  .card {
    position: relative; width: 520px; height: 297px; overflow: hidden;
    box-shadow: 0 10px 24px rgba(0,0,0,0.15);
  }

  /* Front */
  .card-front { background: var(--card-white); }
  .edge-strip {
    position: absolute; left: 0; top: 0; width: 12px; height: 100%;
    background: linear-gradient(to bottom, var(--brand-blue) 0 45%, var(--brand-green) 45% 100%);
  }
  .brand {
    position: absolute; left: 52px; top: 70px;
    display: flex; align-items: center; gap: 12px;
  }
  .brand-square { flex: none; width: 22px; height: 22px; background: var(--brand-blue); }
  .brand-name {
    font-family: "Marcellus SC", serif; font-size: 30px; line-height: 1.05;
    color: var(--brand-blue);
  }
  .brand-name span { display: block; }
  .slogan {
    position: absolute; left: 300px; top: 68px; width: 190px;
    font-family: "Kalam", cursive; font-size: 22px; line-height: 1.25;
    color: var(--brand-green);
  }
  .slogan-underline { display: block; margin-top: 2px; }
  .contact {
    position: absolute; left: 52px; top: 208px;
    font-family: "Marcellus SC", serif; color: var(--text-blue);
    font-size: 14px; line-height: 1.45;
  }
  .contact-role { font-size: 12px; margin-bottom: 2px; }

  /* Back */
  .card-back {
    background: linear-gradient(135deg, var(--brand-blue) 0%, var(--brand-blue-deep) 100%);
  }
  .service-list {
    position: absolute; left: 28px; top: 100px; list-style: none;
    font-family: "Marcellus SC", serif; color: var(--card-white);
    font-size: 15px; line-height: 2;
  }
  .service-list li { display: flex; align-items: center; gap: 10px; }
  .service-list li::before {
    content: ""; width: 18px; height: 1px; background: var(--line-light);
  }
  .back-brand {
    position: absolute; right: 34px; bottom: 40px;
    display: flex; align-items: center; gap: 10px;
  }
  .back-brand .brand-square { width: 16px; height: 16px; background: var(--brand-green); }
  .back-brand .brand-name { font-size: 22px; color: var(--card-white); }
</style>
</head>
<body>
<main class="canvas">
  <section class="card card-front" aria-label="Card front">
    <div class="edge-strip"></div>
    <div class="brand">
      <span class="brand-square"></span>
      <p class="brand-name"><span>Brightacre</span><span>Services</span></p>
    </div>
    <p class="slogan">Your Everything<br>Outside Company
      <svg class="slogan-underline" width="150" height="14" viewBox="0 0 150 14">
        <path d="M4 11 Q60 2 146 4" fill="none" stroke="var(--brand-green)" stroke-width="2" stroke-linecap="round"/>
      </svg>
    </p>
    <div class="contact">
      <p class="contact-role">Salemans</p>
      <p>Phone: 602-417-3859</p>
      <p>Mail: brightacreyard@mailnest.net</p>
    </div>
  </section>

  <section class="card card-back" aria-label="Card back">
    <ul class="service-list">
      <li>Lawn Service</li>
      <li>Fertilization</li>
      <li>Pool Service</li>
      <li>Pressure Washing</li>
    </ul>
    <div class="back-brand">
      <span class="brand-square"></span>
      <span class="brand-name">Brightacre Services</span>
    </div>
  </section>
</main>
</body>
</html>
```